Quarrel Ridge Advisory Business Card

Quarrel Ridge Advisory is a company that provides consulting services to the Mining Industry.

Whilst Quarrel Ridge Advisory is an Australian based company its client base is the global mining industry.

The essence of Quarrel Ridge Advisory is its a can do organisation that can make a difference to its clients by providing quality assistance and form lasting relationships.
Updates

Target Market(s)

The global Mining Industry.

Industry/Entity Type

Mining

Font styles to use
Serif

Colors

Designer to choose colors to be used in the design.

Requirements
Nice to have
• My thinking is the card would look good in black given the logo.

I would like to see written on the back side of the card " Providing Metallurgical, Management and Corporate Services to the Mining Industry"

```html
<!DOCTYPE html>
<html lang="en">
<head>
<meta charset="utf-8">
<title>Quarrel Ridge Advisory – Business Card</title>
<link href="https://fonts.googleapis.com/css2?family=Raleway:wght@300;800&family=Roboto:wght@400;700&display=swap" rel="stylesheet">
<style>
  :root {
    --page: #dcdddf;
    --card-dark: #000000;
    --card-light: #ffffff;
    --accent: #f7a21b;
    --ink-light: #ffffff;
    --ink-dark: #1c1c1c;
  }
  html, body {
    margin: 0;
    padding: 0;
    width: 1200px;
    height: 1200px;
    overflow: hidden;
    background: var(--page);
  }
  .canvas {
    position: relative;
    width: 1200px;
    height: 1200px;
  }
  .card {
    position: absolute;
    left: 174px;
    width: 853px;
    height: 487px;
    overflow: hidden;
  }
  .card--front { top: 69px; background: var(--card-dark); color: var(--ink-light); }
  .card--back  { top: 643px; background: var(--card-light); color: var(--ink-dark); }

  .wordmark {
    position: absolute;
    margin: 0;
    font-family: "Raleway", sans-serif;
    font-weight: 800;
    color: var(--accent);
    text-transform: uppercase;
    line-height: 1.05;
  }
  .card--front .wordmark {
    left: 47px;
    top: 140px;
    font-size: 34px;
    letter-spacing: 1px;
  }
  .card--back .wordmark {
    left: 0;
    right: 0;
    top: 180px;
    text-align: center;
    font-size: 44px;
    letter-spacing: 2px;
  }

  .person {
    position: absolute;
    left: 503px;
    top: 166px;
  }
  .person__name {
    margin: 0;
    font-family: "Raleway", sans-serif;
    font-weight: 300;
    font-size: 42px;
    line-height: 1;
  }
  .person__title {
    margin: 8px 0 0 3px;
    font-family: "Roboto", sans-serif;
    font-weight: 700;
    font-size: 23px;
    letter-spacing: 5px;
  }

  .contact {
    position: absolute;
    left: 49px;
    top: 288px;
    margin: 0;
    padding: 0;
    list-style: none;
    font-family: "Roboto", sans-serif;
    font-size: 23px;
    line-height: 32.5px;
  }

  .tagline {
    position: absolute;
    left: 0;
    right: 0;
    top: 380px;
    margin: 0;
    text-align: center;
    font-family: "Roboto", sans-serif;
    font-size: 24px;
    line-height: 33px;
  }
</style>
</head>
<body>
<main class="canvas">
  <section class="card card--front" aria-label="Card front">
    <p class="wordmark">Quarrel Ridge<br>Advisory</p>
    <div class="person">
      <p class="person__name">Dana Whitlock</p>
      <p class="person__title">PRESIDENT</p>
    </div>
    <ul class="contact">
      <li>1719 Copperbend Road</li>
      <li>Millbrook, NJ 07390</li>
      <li>000-555-0142</li>
      <li>www.QuarrelRidge.com</li>
      <li>DanaWhitlock@QuarrelRidge.com</li>
    </ul>
  </section>

  <section class="card card--back" aria-label="Card back">
    <p class="wordmark">Quarrel Ridge<br>Advisory</p>
    <p class="tagline">Providing Metallurgical, Management and<br>Corporate Services to the Mining Industry</p>
  </section>
</main>
</body>
</html>
```